Gallerine Vault, LLC needs clean, modern business card design

Gallerine Vault is based in Honolulu. We offer fine arts collections management and documentation services for private and corporate art collectors. I would like to use my logo (attached). Card can be either single or double sided and either vertical or horizontal. My clients are businesses with art collections (banks, law firms, etc.) and wealthy individual collectors.

Industry/Entity Type

Business

```html
<!DOCTYPE html>
<html lang="en">
<head>
<meta charset="utf-8">
<title>Gallerine Vault, LLC — Business Card</title>
<link rel="stylesheet" href="https://fonts.googleapis.com/css2?family=Dancing+Script:wght@600&family=Open+Sans:wght@400;700&display=swap">
<style>
  :root {
    --backdrop: #e9e9e7;
    --card: #ffffff;
    --ink: #3a3a3a;
    --ink-soft: #555555;
    --brand-blue: #2f8fd8;
    --icon-dark: #2c3e66;
    --icon-green: #2e9e48;
    --icon-blue: #2f8fd8;
  }
  * { box-sizing: border-box; margin: 0; padding: 0; }
  html, body { width: 1200px; height: 873px; overflow: hidden; }
  body {
    background: var(--backdrop);
    font-family: "Open Sans", Arial, sans-serif;
    color: var(--ink);
    position: relative;
  }
  .card {
    position: absolute;
    top: 282px;
    width: 540px;
    height: 309px;
    background: var(--card);
    box-shadow: 0 6px 18px rgba(0,0,0,0.15);
    overflow: hidden;
  }
  .card--front { left: 40px; }
  .card--back { left: 620px; }

  .card__art { position: absolute; inset: 0; width: 100%; height: 100%; }

  .brand-name {
    font-family: "Open Sans", Arial, sans-serif;
    font-weight: 700;
    color: var(--brand-blue);
    letter-spacing: 0.5px;
    white-space: nowrap;
  }

  /* front */
  .front-brand {
    position: absolute;
    left: 48px;
    top: 110px;
  }
  .front-brand .brand-name { font-size: 38px; }

  /* back */
  .holder {
    position: absolute;
    left: 150px;
    top: 30px;
  }
  .holder__name {
    font-family: "Dancing Script", cursive;
    font-weight: 600;
    font-size: 44px;
    color: var(--brand-blue);
    line-height: 1;
  }
  .holder__title {
    margin-top: 6px;
    margin-left: 52px;
    font-size: 12px;
    font-weight: 700;
    color: var(--ink);
  }
  .contacts {
    position: absolute;
    left: 150px;
    top: 132px;
    list-style: none;
  }
  .contacts li {
    display: flex;
    align-items: center;
    gap: 10px;
    font-size: 12.5px;
    color: var(--ink-soft);
    height: 24px;
  }
  .contact-icon {
    width: 16px; height: 16px;
    border-radius: 50%;
    flex: none;
  }
  .contact-icon--phone { background: var(--icon-blue); }
  .contact-icon--mail { background: var(--icon-green); }
  .contact-icon--web { background: var(--icon-dark); }

  .back-brand {
    position: absolute;
    right: 70px;
    bottom: 26px;
  }
  .back-brand .brand-name { font-size: 17px; }
</style>
</head>
<body>

  <section class="card card--front" aria-label="Card front">
    <svg class="card__art" viewBox="0 0 540 309">
      <defs>
        <linearGradient id="waveFront" x1="0" y1="0" x2="0" y2="1">
          <stop offset="0" stop-color="#1a6fc9"/>
          <stop offset="0.55" stop-color="#2fb3a0"/>
          <stop offset="1" stop-color="#a6cf1c"/>
        </linearGradient>
      </defs>
      <g role="img" aria-label="Flowing blue and green wave with fine light lines">
        <path d="M330 0 H540 V309 H330 C420 250 440 160 400 80 C385 48 360 20 330 0 Z" fill="url(#waveFront)"/>
        <path d="M330 0 C360 20 385 48 400 80 C440 160 420 250 330 309 H318 C405 250 425 160 388 82 C372 50 350 22 322 0 Z" fill="#e6eef5"/>
      </g>
    </svg>
    <div class="front-brand">
      <span class="brand-name">Gallerine Vault</span>
    </div>
  </section>

  <section class="card card--back" aria-label="Card back">
    <svg class="card__art" viewBox="0 0 540 309">
      <defs>
        <linearGradient id="cornerTop" x1="0" y1="0" x2="1" y2="0">
          <stop offset="0" stop-color="#a6cf1c"/>
          <stop offset="1" stop-color="#2f8fd8"/>
        </linearGradient>
        <linearGradient id="cornerBottom" x1="0" y1="0" x2="1" y2="0">
          <stop offset="0" stop-color="#2f8fd8"/>
          <stop offset="1" stop-color="#a6cf1c"/>
        </linearGradient>
      </defs>
      <g role="img" aria-label="Green and blue curved corner accent">
        <path d="M0 309 V240 C50 250 90 280 110 309 Z" fill="url(#cornerTop)"/>
        <path d="M110 309 C90 280 50 250 0 240 V233 C55 244 98 276 118 309 Z" fill="#e3e8ec"/>
      </g>
      <g role="img" aria-label="Green and blue curved corner accent">
        <path d="M400 0 H540 V45 C490 48 430 30 400 0 Z" fill="url(#cornerBottom)"/>
        <path d="M400 0 C430 30 490 48 540 45 V52 C485 55 422 36 392 0 Z" fill="#e3e8ec"/>
      </g>
    </svg>

    <div class="holder">
      <p class="holder__name">Kalani Reyes</p>
      <p class="holder__title">General Manager</p>
    </div>

    <ul class="contacts">
      <li><span class="contact-icon contact-icon--phone"></span>18085550142</li>
      <li><span class="contact-icon contact-icon--mail"></span>info@gallerinevault.com</li>
      <li><span class="contact-icon contact-icon--web"></span>gallerinevault.com/notes</li>
    </ul>

    <div class="back-brand">
      <span class="brand-name">Gallerine Vault</span>
    </div>
  </section>

</body>
</html>
```